Verpackungen für Nahrungsergänzungsmittel
Zielgruppe
Wir vertreiben Nahrungsergänzungsmittel über Apotheken sowie E-commerce Plattformen wie Quorvex.
Aufgabenstellung
Die Verpackungen (Faltschachteln) werden für eine neue Produktlinie (Nahrungsergänzungsmittelserie) benötigt. Also Beispielsweise wird es 3 Produkte geben (Vitamin C, Zink und Eisen). Die genannten Produkte sind lediglich Beispiele. Wichtig bei dem Produktdesign ist, dass ein Element (zum Beispiel) oder ähnliches in jeder Verpackung vorkommt, so dass es einen Wiedererkennungswert für die Marke gibt.
Ein Logo, gesetzliche Pflichtangaben oder Werbetexte spielen erstmal keine Rolle. Es geht in einem ersten Schritt nur darum 'Grunddesigns' zu erstellen. Auch besondere/gewünschte Farben gibt es keine. Es muss einfach nur schön aussehen :-)
Bei Fragen gerne melden..
Ps: Ein Beispielsstanze einer Faltschachtel ist angehängt.

```html
<!DOCTYPE html>
<html lang="de">
<head>
<meta charset="utf-8">
<title>Faltschachteln – Grunddesigns</title>
<link rel="stylesheet" href="https://fonts.googleapis.com/css2?family=Archivo+Black&display=swap">
<style>
  :root {
    --page: #ffffff;
    --sky: #c8e3fa;
    --zinc-yellow: #fae678;
    --iron-pink: #f091b5;
    --vitamin-orange: #f08e68;
    --ink: #000000;
    --edge: #2a2a2a;
  }
  html, body {
    margin: 0;
    padding: 0;
    width: 1200px;
    height: 500px;
    overflow: hidden;
    background: var(--page);
  }
  .canvas {
    position: relative;
    width: 1200px;
    height: 500px;
  }
  .box-front {
    position: absolute;
    top: 22px;
    width: 375px;
    height: 459px;
    display: block;
  }
  .box-front--zinc { left: 13px; }
  .box-front--iron { left: 410px; }
  .box-front--vitamin { left: 809px; }
  .panel-bg { fill: var(--sky); }
  .panel-edge { fill: none; stroke: var(--edge); stroke-width: 3; }
  .shape--zinc { fill: var(--zinc-yellow); }
  .shape--iron { fill: var(--iron-pink); }
  .shape--vitamin { fill: var(--vitamin-orange); }
  .brand-name,
  .product-name,
  .slogan {
    font-family: "Archivo Black", sans-serif;
    fill: var(--ink);
  }
  .brand-name { font-size: 186px; }
  .product-name { font-size: 78px; }
  .slogan { font-size: 17px; }
</style>
</head>
<body>
<main class="canvas">

  <svg class="box-front box-front--zinc" viewBox="0 0 657 804" aria-label="Verpackung Zink">
    <defs><clipPath id="clip-zinc"><rect width="657" height="804"/></clipPath></defs>
    <rect class="panel-bg" width="657" height="804"/>
    <g clip-path="url(#clip-zinc)">
      <ellipse class="shape--zinc" cx="0" cy="215" rx="293" ry="188"/>
      <ellipse class="shape--zinc" cx="0" cy="602" rx="293" ry="188"/>
      <ellipse class="shape--zinc" cx="657" cy="215" rx="293" ry="188"/>
      <ellipse class="shape--zinc" cx="657" cy="602" rx="293" ry="188"/>
    </g>
    <text class="brand-name" transform="translate(478 164) rotate(90)" textLength="470" lengthAdjust="spacingAndGlyphs">name</text>
    <text class="product-name" transform="translate(36 329) rotate(90)" textLength="160" lengthAdjust="spacingAndGlyphs">zink</text>
    <text class="slogan" transform="translate(309 337) rotate(90)" textLength="177" lengthAdjust="spacingAndGlyphs">hier steht zB ein slogan</text>
    <rect class="panel-edge" width="657" height="804"/>
  </svg>

  <svg class="box-front box-front--iron" viewBox="0 0 657 804" aria-label="Verpackung Eisen">
    <defs><clipPath id="clip-iron"><rect width="657" height="804"/></clipPath></defs>
    <rect class="panel-bg" width="657" height="804"/>
    <g clip-path="url(#clip-iron)">
      <ellipse class="shape--iron" cx="0" cy="215" rx="293" ry="188"/>
      <ellipse class="shape--iron" cx="0" cy="602" rx="293" ry="188"/>
      <ellipse class="shape--iron" cx="657" cy="215" rx="293" ry="188"/>
      <ellipse class="shape--iron" cx="657" cy="602" rx="293" ry="188"/>
    </g>
    <text class="brand-name" transform="translate(478 164) rotate(90)" textLength="470" lengthAdjust="spacingAndGlyphs">name</text>
    <text class="product-name" transform="translate(46 325) rotate(90)" textLength="184" lengthAdjust="spacingAndGlyphs">eisen</text>
    <text class="slogan" transform="translate(331 348) rotate(90)" textLength="178" lengthAdjust="spacingAndGlyphs">hier steht zB ein slogan</text>
    <rect class="panel-edge" width="657" height="804"/>
  </svg>

  <svg class="box-front box-front--vitamin" viewBox="0 0 657 804" aria-label="Verpackung Vitamin C">
    <defs><clipPath id="clip-vitamin"><rect width="657" height="804"/></clipPath></defs>
    <rect class="panel-bg" width="657" height="804"/>
    <g clip-path="url(#clip-vitamin)">
      <ellipse class="shape--vitamin" cx="0" cy="215" rx="293" ry="188"/>
      <ellipse class="shape--vitamin" cx="0" cy="602" rx="293" ry="188"/>
      <ellipse class="shape--vitamin" cx="657" cy="215" rx="293" ry="188"/>
      <ellipse class="shape--vitamin" cx="657" cy="602" rx="293" ry="188"/>
    </g>
    <text class="brand-name" transform="translate(478 173) rotate(90)" textLength="468" lengthAdjust="spacingAndGlyphs">name</text>
    <text class="product-name" transform="translate(42 248) rotate(90)" textLength="331" lengthAdjust="spacingAndGlyphs">vitamin c</text>
    <text class="slogan" transform="translate(323 329) rotate(90)" textLength="178" lengthAdjust="spacingAndGlyphs">hier steht zB ein slogan</text>
    <rect class="panel-edge" width="657" height="804"/>
  </svg>

</main>
</body>
</html>
```